Verdelle Chronicles - epic fantasy adventure cover

I am an author of a teen-young-adult epic fantasy trilogy. I have written the first book to my second trilogy in the same world and are looking for a new artist for the entire trilogy. Of course there is only one book right now but I’d be looking for someone who would be willing to see the trilogy through with me and also put together a design that fits with the first set.

I have uploaded my first books and a design my original designer came up with but then was unable to complete the project. I would like something like this but not to use the picture from my last artist as I am only posting as a reference.

Two of the main characters are
Orivel - a half elvin wizard (elf ears, large blue elvin eyes, shoulder length black scruffy hair with red tufts, tall like a human) He wears a blue stone around his neck as seen by other books. In fact book 3 with the child on it is him as a 8 year old... He is now 28
Lunavene - half elvin sister of Orivel with magic abilities (elf ears, large green elf eyes, long red hair with little braids throughout it, slightly taller than Orivel) she carrys a long sword on her back and has two short swords that she has strapped to her thighs. She is 21
One or both siblings could appear on the cover.

Some extras
Reminder that this is a teen read so not too sexy, although they are attractive people.

I am looking for something that sits between real and not real… I don’t want something that looks cartoonish but on the other hand I don’t want real photos of people, something that looks kind of real but is obviously not.

Teen to Young adult with an appeal to all ages as all ages read my books

Serif

0054AA
0677BA
7BADD7
CADEEF
E8F1F8
00AB8E
00BBA5
67D7C9
C6EFE9
E9F9F6

• Largest series title = Verdelle Chronicles *next largest book title = Echoes of Cinderfall *Small Author name = Moira Tolvane * one or both of the main characters on the cover *book 1
• *shadow of a dragon in the distance *a small old ship in distance or on back cover *maybe a long shadow or two on the front or back cover
• Not be cartoonish or surreal

```html
<!DOCTYPE html>
<html lang="en">
<head>
<meta charset="utf-8">
<title>Verdelle Chronicles – Echoes of Cinderfall, cover wrap</title>
<link rel="stylesheet" href="https://fonts.googleapis.com/css2?family=Cinzel:wght@400;700&family=Great+Vibes&family=Playfair+Display:wght@400&display=swap">
<style>
  :root {
    --stage: #38343e;
    --cover-ink: #17131f;
    --cover-deep: #0f0c16;
    --text-light: #f1eef4;
    --spine-title: #b8461f;
    --spine-author: #8e8a94;
    --gold-light: #e6d3a6;
    --gold: #c5a66a;
    --sky-gold: #e0a23a;
    --sky-amber: #a8681f;
    --sea-brown: #4e3218;
    --brief-blue: #0054aa;
    --brief-blue-mid: #0677ba;
    --brief-teal: #00ab8e;
    --brief-teal-light: #67d7c9;
    --cloak-deep: #0d2a33;
  }
  * { box-sizing: border-box; margin: 0; padding: 0; }
  html, body { width: 1200px; height: 960px; overflow: hidden; }
  body { background: var(--stage); position: relative; }

  .cover-wrap {
    position: absolute; left: 168px; top: 160px;
    width: 864px; height: 640px;
    display: flex;
    box-shadow: 0 24px 50px rgba(0,0,0,.45);
  }

  /* Back cover */
  .back-cover {
    position: relative; width: 400px; height: 100%;
    background: var(--cover-ink); overflow: hidden;
    color: var(--text-light);
    font-family: "Playfair Display", Georgia, serif;
    text-align: center;
  }
  .back-art {
    position: absolute; inset: 0;
    background:
      radial-gradient(ellipse 55% 70% at 40% 38%, rgba(120,112,132,.26), transparent 70%),
      linear-gradient(180deg, #221d2c 0%, var(--cover-ink) 100%);
  }
  .back-heading {
    position: relative; margin-top: 26px;
    font-family: "Great Vibes", cursive;
    font-size: 58px; font-weight: 400; line-height: 1;
  }
  .back-blurb { position: relative; padding: 22px 32px 0; }
  .back-blurb p { font-size: 13px; line-height: 1.34; margin-bottom: 19px; }

  /* Spine */
  .spine {
    position: relative; width: 64px; height: 100%;
    background: var(--cover-deep);
    display: flex; align-items: center; justify-content: center;
  }
  .spine-text {
    transform: rotate(-90deg); white-space: nowrap;
    display: flex; flex-direction: column; align-items: center; gap: 4px;
  }
  .spine-title {
    font-family: "Cinzel", Georgia, serif; font-size: 24px;
    color: var(--spine-title); letter-spacing: .5px;
  }
  .spine-author {
    font-family: "Cinzel", Georgia, serif; font-size: 10px;
    color: var(--spine-author); letter-spacing: 4px;
  }

  /* Front cover */
  .front-cover {
    position: relative; width: 400px; height: 100%;
    background: var(--cover-ink); overflow: hidden;
    text-align: center;
  }
  .front-art {
    position: absolute; inset: 0 0 22% 0;
    background:
      radial-gradient(ellipse 38% 50% at 50% 66%, var(--cloak-deep) 0%, rgba(6,119,186,.18) 55%, transparent 78%),
      radial-gradient(ellipse 60% 22% at 50% 98%, rgba(0,171,142,.18), transparent 75%),
      linear-gradient(180deg,
        #5c4020 0%,
        var(--sky-gold) 16%,
        var(--sky-amber) 30%,
        var(--sea-brown) 38%,
        #3a2a22 55%,
        #1f1a28 80%,
        var(--cover-ink) 100%);
  }
  .front-art::after {
    content: ""; position: absolute; inset: 0;
    background: linear-gradient(180deg, transparent 70%, var(--cover-ink) 100%);
  }
  .series-title {
    position: absolute; left: 0; right: 0; top: 412px;
    font-family: "Cinzel", Georgia, serif; font-weight: 700;
    color: var(--gold-light);
    text-shadow: 0 2px 3px rgba(0,0,0,.6);
    line-height: 1;
  }
  .series-title .line-one { display: block; font-size: 50px; letter-spacing: 1px; }
  .series-title .line-two { display: block; font-size: 40px; margin-top: 26px; }
  .title-rule { position: absolute; left: 70px; top: 472px; }
  .book-title {
    position: absolute; left: 0; right: 0; top: 556px;
    font-family: "Cinzel", Georgia, serif; font-size: 22px; font-weight: 400;
    color: var(--gold); letter-spacing: 1px;
  }
  .author-name {
    position: absolute; left: 0; right: 0; top: 588px;
    font-family: "Cinzel", Georgia, serif; font-size: 12px;
    color: var(--gold-light); letter-spacing: 4px;
  }
</style>
</head>
<body>
  <main class="cover-wrap">
    <section class="back-cover">
      <div class="back-art" role="img" aria-label="Faint grey dragon silhouette fading into the dark background"></div>
      <h2 class="back-heading">Free</h2>
      <div class="back-blurb">
        <p>Lorem ipsum dolor sit amet, consectetur adipiscing elit, sed do eiusmod tempor incididunt ut labore et dolore magna aliqua. Quis ipsum suspendisse ultrices gravida. Risus commodo viverra maecenas accumsan lacus vel facilisis. Lore incididunt ut labore et dolore magna aliqua. Quis ipsum suspendisse ultrices gravida. Risus commodo viverra maecenas accumsan lacus vel facilisis.</p>
        <p>Lorem ipsum dolor sit amet, consectetur adipiscing elit, sed do eiusmod tempor incididunt ut labore et dolore magna aliqua. Quis ipsum suspendisse ultrices gravida. Risus commodo viverra maecenas accumsan lacus vel facilisis.</p>
        <p>Lorem ipsum dolor sit amet, consectetur adipiscing elit, sed do eiusmod tempor incididunt ut labore et dolore magna aliqua. Quis ipsum suspendisse ultrices gravida. Risus commodo viverra maecenas accumsan lacus vel facilisis. Lorem ipsum dolor sit amet, consectetur adipiscing elit, sed do eiusmod tempor incididunt ut labore et dolore magna aliqua. Quis ipsum suspendisse ultrices gravida. Risus commodo viverra maecenas accumsan lacus vel facilisis.</p>
        <p>Lorem ipsum dolor sit ae ultrices gravida. Risus commodo viverra maecenas accumsan lacus vel facilisis.</p>
      </div>
    </section>

    <section class="spine">
      <div class="spine-text">
        <span class="spine-title">ROAD OF TIDESTONE</span>
        <span class="spine-author">MOIRA TOLVANE</span>
      </div>
    </section>

    <section class="front-cover">
      <div class="front-art" role="img" aria-label="Hooded red-haired half-elf woman in a dark teal cloak holding a long sword upright before her face, a dragon and an old sailing ship on a golden sunset sea behind her"></div>
      <h1 class="series-title">
        <span class="line-one">VERDELLE</span>
        <span class="line-two">CHRONICLES</span>
      </h1>
      <svg class="title-rule" width="260" height="12" viewBox="0 0 260 12" aria-hidden="true">
        <line x1="0" y1="6" x2="260" y2="6" stroke="#c5a66a" stroke-width="1.5"/>
        <circle cx="130" cy="6" r="3" fill="#c5a66a"/>
      </svg>
      <h2 class="book-title">ECHOES OF CINDERFALL</h2>
      <p class="author-name">MOIRA TOLVANE</p>
    </section>
  </main>
</body>
</html>
```